new private customer brochure

New brochure for advertising our services in bathroom remodeling, heating system renovation, and ventilation cleaning. Brochure size A5 with 4 pages. More informations about the company will you see on the website: www.talbrunex.ch

```html
<!DOCTYPE html>
<html lang="de">
<head>
<meta charset="utf-8">
<title>Talbrunex Broschüre</title>
<link rel="stylesheet" href="https://fonts.googleapis.com/css2?family=Source+Sans+3:wght@400;600;700&display=swap">
<style>
:root{
  --bg:#8a8a8a;
  --paper:#ffffff;
  --ink:#3a3a3a;
  --ink-dark:#1d1d1d;
  --yellow:#f7c800;
  --red:#e2003a;
  --green:#007b55;
  --blue:#1d86d0;
  --orange:#f28c00;
  --ring:#e4e6e8;
}
*{margin:0;padding:0;box-sizing:border-box}
html,body{width:1200px;height:493px;overflow:hidden;background:var(--bg);font-family:"Source Sans 3",sans-serif;color:var(--ink)}
.page{position:absolute;top:40px;height:418px;background:var(--paper)}
.page--left{left:7px;width:589px}
.page--right{left:600px;width:588px}
.services{position:absolute;inset:0;width:589px;height:418px}
.services text{font-family:"Source Sans 3",sans-serif}
.service-label{font-size:9.5px;fill:var(--ink);text-anchor:middle}
.photo{position:absolute;left:5px;top:5px;width:275px;height:407px;
  background:linear-gradient(100deg,#b9bcb8 0%,#8d918c 25%,#a9b3a0 45%,#5e6a55 65%,#3f4241 85%,#2e3030 100%)}
.copy{position:absolute;left:294px;top:55px;width:275px}
.copy__title{font-size:22px;font-weight:700;color:var(--yellow);line-height:1;letter-spacing:.3px}
.copy__lead{font-size:12px;color:var(--ink-dark);line-height:15px;margin-top:4px}
.copy__text{font-size:8.7px;line-height:11.6px;text-align:justify;margin-top:17px}
.copy__text + .copy__text{margin-top:11px}
.copy__caps{font-size:8.7px;margin-top:12px;text-transform:uppercase}
.feature{display:flex;align-items:center;gap:14px;margin-top:12px}
.feature:first-of-type{margin-top:13px}
.feature__icon{flex:0 0 30px;width:30px;height:30px}
.feature__text{font-size:8.7px;line-height:11.6px}
.color-bar{position:absolute;left:295px;top:393px;width:281px;height:5px;display:flex}
.color-bar span{flex:1}
</style>
</head>
<body>

<section class="page page--left">
  <svg class="services" viewBox="0 0 589 418" aria-label="Leistungsübersicht">
    <defs>
      <radialGradient id="ringShade" cx="0.6" cy="0.6" r="0.6">
        <stop offset="0" stop-color="#f2f3f4"/>
        <stop offset="1" stop-color="#cfd2d5"/>
      </radialGradient>
      <filter id="soft" x="-20%" y="-20%" width="140%" height="140%">
        <feDropShadow dx="3" dy="4" stdDeviation="4" flood-color="#000" flood-opacity=".18"/>
      </filter>
    </defs>

    <!-- hub -->
    <circle cx="290" cy="135" r="94" fill="url(#ringShade)"/>
    <circle cx="290" cy="135" r="72" fill="#fff" filter="url(#soft)"/>
    <text x="290" y="129" text-anchor="middle" font-size="11" font-weight="700" fill="var(--yellow)">TALBRUNEX</text>
    <text x="290" y="143" text-anchor="middle" font-size="11" fill="var(--ink-dark)">Gebäude-Kompetenz</text>
    <rect x="243" y="150" width="94" height="58" rx="6" fill="#dfe6ee" role="img" aria-label="Illustration eines Hauses mit Solardach, Haustechnik und Elektroauto"/>

    <!-- connecting arc -->
    <g fill="none" stroke-width="2.4">
      <path d="M186 173 A112 112 0 0 0 227 224" stroke="var(--green)"/>
      <path d="M227 224 A112 112 0 0 0 290 244" stroke="var(--yellow)"/>
      <path d="M290 244 A112 112 0 0 0 352 224" stroke="var(--blue)"/>
      <path d="M352 224 A112 112 0 0 0 393 173" stroke="var(--orange)"/>
    </g>
    <circle cx="186" cy="173" r="7" fill="var(--red)"/>
    <circle cx="227" cy="224" r="7" fill="var(--yellow)"/>
    <circle cx="290" cy="244" r="7" fill="var(--green)"/>
    <circle cx="352" cy="224" r="7" fill="var(--blue)"/>
    <circle cx="393" cy="173" r="7" fill="var(--orange)"/>

    <!-- heating -->
    <path d="M152 181 L168 183 L158 194 Z" fill="var(--red)"/>
    <circle cx="122" cy="195" r="37" fill="var(--red)"/>
    <circle cx="122" cy="195" r="25" fill="#fff"/>
    <path d="M122 180 C131 189 133 196 131 202 C129 208 115 209 113 202 C111 196 115 191 117 188 C118 193 121 194 122 192 C124 188 121 184 122 180 Z" fill="var(--red)"/>
    <text class="service-label" x="111" y="250">Heizungsersatz</text>

    <!-- sanitary -->
    <path d="M212 243 L214 259 L203 252 Z" fill="var(--yellow)"/>
    <circle cx="189" cy="282" r="37" fill="var(--yellow)"/>
    <circle cx="189" cy="282" r="25" fill="#fff"/>
    <g fill="none" stroke="var(--yellow)" stroke-width="1.6">
      <rect x="196" y="270" width="5" height="12"/>
      <path d="M177 282 H201 C200 290 195 292 190 292 V296 H184 V292 C180 291 177 287 177 282 Z"/>
    </g>
    <text class="service-label" x="180" y="340">Ersatz sanitäre Anlagen</text>

    <!-- ventilation -->
    <path d="M291 269 L297 281 L285 281 Z" fill="var(--green)"/>
    <circle cx="291" cy="317" r="37" fill="var(--green)"/>
    <circle cx="291" cy="317" r="25" fill="#fff"/>
    <g fill="none" stroke="var(--green)" stroke-width="1.4">
      <rect x="280" y="303" width="22" height="22" rx="2"/>
      <circle cx="291" cy="314" r="7"/>
      <path d="M291 307 V321 M284 314 H298"/>
      <path d="M282 325 V330 M300 325 V330"/>
    </g>
    <text class="service-label" x="290" y="373">Lüftungsanlagenersatz</text>

    <!-- photovoltaics -->
    <path d="M366 243 L378 254 L365 258 Z" fill="var(--blue)"/>
    <circle cx="391" cy="282" r="37" fill="var(--blue)"/>
    <circle cx="391" cy="282" r="25" fill="#fff"/>
    <g fill="none" stroke="var(--blue)" stroke-width="1.2">
      <circle cx="384" cy="275" r="3.5"/>
      <path d="M389 275 H393 M384 269 V270"/>
      <path d="M383 281 H403 L399 291 H379 Z"/>
      <path d="M388 281 L384 291 M393 281 L389 291 M398 281 L394 291 M381 286 H401"/>
      <path d="M385 291 V295 M397 291 V295"/>
    </g>
    <text class="service-label" x="406" y="340">Photovoltaik Anlagen</text>

    <!-- roof -->
    <path d="M413 183 L428 176 L426 192 Z" fill="var(--orange)"/>
    <circle cx="456" cy="195" r="37" fill="var(--orange)"/>
    <circle cx="456" cy="195" r="25" fill="#fff"/>
    <g fill="none" stroke="var(--orange)" stroke-width="1.6">
      <path d="M443 195 L456 183 L469 195"/>
      <path d="M446 193 V207 H466 V193"/>
      <path d="M453 207 V199 H459 V207"/>
    </g>
    <text class="service-label" x="470" y="250">Dach- und Fassade</text>
  </svg>
</section>

<section class="page page--right">
  <div class="photo" role="img" aria-label="Foto eines Handwerkers mit gelbem Helm, der am Baugerüst eine Markierung an der Wand anbringt"></div>

  <div class="copy">
    <h1 class="copy__title">BADUMBAU</h1>
    <p class="copy__lead">Ein neues Traumbad für die eigenen vier Wände?<br>Wir bauen es für Sie innert kurzer Zeit…</p>
    <p class="copy__text">Im Badezimmer sind die Armaturen verkratzt, die Duschtrennwand rinnt, die Badewanne defekt oder Sie haben einfach Lust, Ihr Badezimmer neu zu gestalten? Wir unterstützen Sie bei Ihrem Badumbau von der Planung über die Beratung bis zur Ausführung.</p>
    <p class="copy__text">Für eine noch genauere Umsetzung Ihrer Idee, visualisieren wir für Sie eine 3D-Badgestaltung. Erleben Sie Ihr neues Badezimmer in Farbe, Form, Material und Licht noch vor dem Umbau. Mit unserer Bad-Kalkulator erhalten Sie in wenigen Schritten eine erste Kosten­schätzung.</p>
    <p class="copy__caps">Ihren Badumbau planen, koordinieren und realisieren</p>

    <div class="feature">
      <svg class="feature__icon" viewBox="0 0 30 30" aria-hidden="true">
        <circle cx="15" cy="15" r="15" fill="var(--ink-dark)"/>
        <g fill="none" stroke="var(--yellow)" stroke-width="1.2">
          <rect x="8" y="9" width="14" height="10"/>
          <rect x="10" y="11" width="4" height="4"/>
          <rect x="16" y="11" width="4" height="4"/>
          <path d="M15 19 V22 M11 22 H19"/>
        </g>
      </svg>
      <p class="feature__text">Alles aus einer Hand. Wir planen und gestalten nach Ihren Wünschen.</p>
    </div>

    <div class="feature">
      <svg class="feature__icon" viewBox="0 0 30 30" aria-hidden="true">
        <circle cx="15" cy="15" r="15" fill="var(--ink-dark)"/>
        <g fill="var(--yellow)">
          <circle cx="9" cy="10" r="2.2"/>
          <circle cx="15" cy="9" r="2.5"/>
          <circle cx="21" cy="10" r="2.2"/>
          <rect x="6.5" y="13" width="5" height="8" rx="2"/>
          <rect x="12.3" y="12.5" width="5.4" height="10" rx="2.2"/>
          <rect x="18.5" y="13" width="5" height="8" rx="2"/>
        </g>
      </svg>
      <p class="feature__text">Wir organisieren und koordinieren alle Arbeiten mit den beteiligten Fachleuten.</p>
    </div>
  </div>

  <div class="color-bar" aria-hidden="true">
    <span style="background:var(--green)"></span>
    <span style="background:var(--red)"></span>
    <span style="background:var(--blue)"></span>
    <span style="background:var(--orange)"></span>
  </div>
</section>

</body>
</html>
```